Personal contact Business card design needed

I work in the Property Industry - specifically Property Management.

I need a card I can hand out to colleagues at networking events, meetings, training courses etc. that will provide my contact details.

Target Market(s)

Professional colleagues / potential clients / employers

Industry/Entity Type

Training

Contact Information for Business Card

I need a simple and professional card to give to professional network contacts at meetings, interviews etc.

The card should include my photograph, name, mobile number, email address and Careerloom address.

I would like appropriate professional colours. Something feminine but not too 'frilly' or 'girly'

Requirements
Must have
• Photograph of myself.
I want it to be simple,perhaps a small icon for each contact detail such as
Email icon
Careerloom icon
Mobile number

```html
<!DOCTYPE html>
<html lang="en">
<head>
<meta charset="utf-8">
<title>Maren Holt – Business Card</title>
<link rel="stylesheet" href="https://fonts.googleapis.com/css2?family=Quicksand:wght@400;500;700&family=Nanum+Pen+Script&family=Schoolbell&display=swap">
<style>
  :root {
    --backdrop: #3b3e41;
    --card: #f4f3f1;
    --plum: #8e1f6b;
    --plum-light: #a8307f;
    --ink: #2b2b2b;
    --grey: #5a5a5a;
    --band-edge: #1e1e1e;
  }
  * { margin: 0; padding: 0; box-sizing: border-box; }
  html, body {
    width: 1200px; height: 1000px; overflow: hidden;
    background: var(--backdrop);
  }
  .card {
    position: absolute; left: 100px; top: 214px;
    width: 1000px; height: 572px;
    background: var(--card);
    overflow: hidden;
    font-family: "Quicksand", sans-serif;
    color: var(--ink);
  }
  .card__shapes { position: absolute; inset: 0; }
  .label-name {
    position: absolute; left: 44px; top: 26px;
    font-size: 28px; font-weight: 500; color: var(--grey);
    line-height: 1.2;
  }
  .holder-name {
    position: absolute; left: 44px; top: 62px;
    font-family: "Schoolbell", cursive;
    font-size: 40px; color: var(--plum); letter-spacing: 2px;
    line-height: 1.2; white-space: nowrap;
  }
  .note {
    position: absolute;
    font-family: "Nanum Pen Script", cursive;
    color: var(--ink);
    line-height: 1.1; white-space: nowrap;
  }
  .note--me { left: 44px; top: 142px; font-size: 38px; }
  .note--contact { left: 436px; top: 160px; font-size: 36px; }
  .note--profile { left: 60px; top: 360px; font-size: 40px; }
  .portrait {
    position: absolute; left: 48px; top: 196px;
    width: 200px; height: 150px;
    background: linear-gradient(160deg, #e9e6e3 0%, #cfc6c2 45%, #4a3433 75%, #1f1a1c 100%);
  }
  .contact-band {
    position: absolute; left: 432px; top: 200px;
    width: 532px; height: 88px;
    background: var(--plum);
    border-left: 7px solid var(--band-edge);
    color: #fff;
    padding: 10px 0 0 40px;
    font-size: 26px; font-weight: 400;
  }
  .contact-band__row {
    display: flex; align-items: center; gap: 16px;
    height: 34px; white-space: nowrap;
  }
  .contact-band__row svg { flex: none; }
  .profile {
    position: absolute; left: 46px; top: 436px;
    display: flex; align-items: baseline; gap: 16px;
    white-space: nowrap; line-height: 1.1;
  }
  .profile__network {
    font-size: 32px; font-weight: 700; color: var(--plum);
  }
  .profile__url {
    font-size: 23px; color: var(--grey);
  }
  .profile__url strong { color: var(--ink); font-weight: 700; }
</style>
</head>
<body>
  <div class="card">
    <svg class="card__shapes" width="1000" height="572" viewBox="0 0 1000 572">
      <polygon points="0,550 1000,472 1000,572 0,572" fill="var(--plum)"/>
      <polygon points="560,506 1000,472 1000,478" fill="var(--plum-light)"/>
      <g fill="none" stroke="var(--ink)" stroke-width="2.5" stroke-linecap="round">
        <path d="M142 40 C162 26, 192 32, 182 58"/>
        <path d="M172 50 L182 60 L192 48"/>
        <path d="M268 170 C300 192, 310 240, 290 290"/>
        <path d="M278 276 L290 292 L304 278"/>
        <path d="M742 362 C792 350, 812 400, 782 420 C767 430, 754 430, 742 426"/>
        <path d="M754 416 L742 426 L756 434"/>
      </g>
    </svg>

    <div class="label-name">Name:</div>
    <div class="holder-name">Maren Holt</div>

    <div class="note note--me">This is me:</div>
    <div class="portrait" role="img" aria-label="Portrait photograph of Maren Holt"></div>

    <div class="note note--contact">contact me</div>
    <div class="contact-band">
      <div class="contact-band__row">
        <svg width="26" height="20" viewBox="0 0 26 20" aria-hidden="true">
          <path d="M2 8 C2 2, 24 2, 24 8 L19 9 L18 6 C14 5, 12 5, 8 6 L7 9 Z" fill="#fff"/>
          <rect x="5" y="10" width="16" height="9" rx="2" fill="#fff"/>
          <circle cx="13" cy="14.5" r="2.5" fill="var(--plum)"/>
        </svg>
        <span>0400 555 019</span>
      </div>
      <div class="contact-band__row">
        <svg width="26" height="18" viewBox="0 0 26 18" aria-hidden="true">
          <rect x="1" y="1" width="24" height="16" fill="#fff"/>
          <path d="M1 1 L13 10 L25 1" fill="none" stroke="var(--plum)" stroke-width="1.8"/>
        </svg>
        <span>maren@holtmail.com.au</span>
      </div>
    </div>

    <div class="note note--profile">And this is my Careerloom profile</div>
    <div class="profile">
      <span class="profile__network">Careerloom</span>
      <span class="profile__url">au.careerloom.com/in/<strong>marenholtaustralia</strong></span>
    </div>
  </div>
</body>
</html>
```